We need banner ads in different sizes for a boat sales event on Grand Lake, OK. People will need to go to 5 different locations and they have the option if they go to all the stops of winning a $2000 tropical travel voucher. Most of the boats are 30' yachts such as WaveKite, Corvant, Helmstrand, Dolan Marsh brands plus jet ski.

Please do not use more than 7 elements.
Name - Tide and Tally Dockside Boat Fair
April 29-May 1st
Grand Lake, Oklahoma
Over 100 new and pre-owned boats at 5 locations and 7 boat dealers

Standard Ad Unit Sizes – W X H
Inline Rectangle
300 X 250
Leaderboard
728 X 90
Large Rectangle
336 X 280
Wide Skyscraper
160 X 600
Banner
468 X 60
Skyscraper
120 X 600
Square
250 X 250
Small Square
200 X 200

· Maximum file size is 150KB for each ad.

· Acceptable file types for non-animated ads: .jpg (my preferred), .png and .gif

Target Market(s)

Men in their 30-50 Range

Industry/Entity Type

Event

Font styles to use
Serif

Colors
0255a3
85cae6
33b8a4

Requirements
Must have
• Logo, Date, Boat or nautical element and win a tropical travel voucher
Nice to have
• Map of locations
Should not have
• Does not need to have website on the ad

```html
<!DOCTYPE html>
<html lang="en">
<head>
<meta charset="utf-8">
<title>Tide and Tally Dockside Boat Fair – Banner Set</title>
<link href="https://fonts.googleapis.com/css2?family=Oswald:wght@400;500&display=swap" rel="stylesheet">
<style>
:root{
  --teal:#1a9aad;
  --white:#ffffff;
  --gold:#f2d57e;
  --pink:#f5a9d9;
  --rim:#e9dca6;
  --label:#222222;
  --btn-top:#f6e39a;
  --btn-bottom:#d8b55a;
  --sky:#d9e7ef;
  --sofa:#e8e0d4;
  --hull:#3a4a66;
  --sea:#3cc3cf;
}
*{box-sizing:border-box;margin:0;padding:0}
html,body{width:1200px;height:1200px;overflow:hidden;background:var(--white)}
body{font-family:"Oswald",sans-serif;text-transform:uppercase}
.stage{position:relative;width:1100px;height:1100px;transform:scale(1.0909);transform-origin:0 0}
.size-label{position:absolute;font-size:13px;font-weight:400;color:var(--label);transform:translateX(-50%);letter-spacing:.2px}
.ad{position:absolute;background:var(--teal);overflow:hidden;color:var(--white);font-weight:500}
.photo-kids{background:linear-gradient(180deg,var(--sky) 0%,#f1ece4 45%,var(--sofa) 100%)}
.photo-boat{background:linear-gradient(180deg,#e4e8ee 0%,#9aa6b8 45%,var(--hull) 70%,#cfd6de 100%)}
.photo-tropic{background:linear-gradient(180deg,#8fc6ea 0%,#cfe8f4 45%,var(--sea) 62%,#1aa2b8 100%)}

/* leaderboard */
.leader{left:26px;width:728px;height:90px}
.leader .photo{position:absolute;left:0;top:0;width:248px;height:90px;border-right:4px solid var(--rim);border-radius:0 70px 70px 0/0 45px 45px 0}
.brand-mark{font-size:13px;line-height:1.15;letter-spacing:1px;text-align:center;color:var(--white);font-weight:500}
.leader .brand-mark{position:absolute;left:272px;top:24px;width:160px}
.leader .headline{position:absolute;left:430px;right:0;top:0;height:90px;display:flex;flex-direction:column;justify-content:center;align-items:center;text-align:center;font-size:20px;line-height:24px}

/* rectangle */
.rect{left:771px;width:300px;height:250px}
.rect .photo{position:absolute;left:0;top:0;width:300px;height:130px;border-bottom:4px solid var(--rim);border-radius:0 0 50% 50%/0 0 14px 14px}
.rect .brand-mark{position:absolute;right:8px;top:12px;width:92px;font-size:9px;color:var(--teal)}
.rect .headline{position:absolute;left:0;right:0;top:134px;bottom:0;display:flex;flex-direction:column;justify-content:center;align-items:center;text-align:center;font-size:21px;line-height:29px;padding:0 8px}

/* skyscraper */
.sky{top:443px;width:160px;height:599px}
.sky .photo{position:absolute;left:0;top:0;width:160px;height:198px;border-bottom:4px solid var(--rim);border-radius:0 0 50% 50%/0 0 14px 14px}
.sky .brand-mark{position:absolute;left:8px;right:8px;top:245px;font-size:14px}
.sky .headline{position:absolute;left:0;right:0;top:330px;bottom:40px;display:flex;flex-direction:column;justify-content:center;align-items:center;text-align:center;font-size:20px;line-height:30px;padding:0 6px}

.gold{color:var(--gold)}
.pink{color:var(--pink)}
.more-info{display:inline-block;margin-top:4px;padding:0 10px;font-size:15px;line-height:22px;font-weight:400;color:var(--white);background:linear-gradient(180deg,var(--btn-top),var(--btn-bottom));border:1px solid #fff6d2;letter-spacing:.3px}
</style>
</head>
<body>
<div class="stage">

  <span class="size-label" style="left:400px;top:24px">728 x 90 pixel</span>

  <div class="ad leader" style="top:52px">
    <div class="photo photo-kids" role="img" aria-label="Two children in life jackets cheering on a pontoon boat sofa"></div>
    <div class="brand-mark">Tide and Tally<br>Dockside Boat Fair</div>
    <div class="headline"><span>Tide and Tally Dockside Boat Fair</span><span>sets sail on <span class="gold">Grand Lake, OK. April 29th - May 1st</span></span></div>
  </div>

  <div class="ad leader" style="top:170px">
    <div class="photo photo-boat" role="img" aria-label="Navy pontoon boat cruising on the lake"></div>
    <div class="brand-mark">Tide and Tally<br>Dockside Boat Fair</div>
    <div class="headline"><span><span class="gold">Over 100</span> new and pre-owned</span><span>boats at <span class="gold">5 locations</span> and <span class="gold">7</span></span><span class="pink">boat dealers</span></div>
  </div>

  <div class="ad leader" style="top:288px">
    <div class="photo photo-tropic" role="img" aria-label="Yachts anchored on turquoise tropical water"></div>
    <div class="brand-mark" style="left:300px">Tide and Tally<br>Dockside Boat Fair</div>
    <div class="headline" style="left:460px;right:40px"><span>Win a <span class="gold">tropical travel</span></span><span class="gold">voucher <span style="color:var(--white)">for</span> $2000</span><span class="more-info">More info</span></div>
  </div>

  <div class="ad rect" style="top:138px">
    <div class="photo photo-kids" role="img" aria-label="Two children in life jackets cheering on a pontoon boat sofa"></div>
    <div class="brand-mark">Tide and Tally<br>Dockside Boat Fair</div>
    <div class="headline" style="font-size:19px;line-height:28px"><span>Tide and Tally Dockside Boat Fair</span><span>sets sail on <span class="gold">Grand Lake,</span></span><span class="gold">OK. April 29th - May 1st</span></div>
  </div>

  <div class="ad rect" style="top:405px">
    <div class="photo photo-boat" role="img" aria-label="Navy pontoon boat cruising on the lake"></div>
    <div class="brand-mark">Tide and Tally<br>Dockside Boat Fair</div>
    <div class="headline"><span><span class="gold">Over 100</span> new and pre-owned</span><span>boats at <span class="gold">5 locations</span> and <span class="gold">7</span></span><span class="pink">boat dealers</span></div>
  </div>

  <div class="ad rect" style="top:673px">
    <div class="photo photo-tropic" role="img" aria-label="Yachts anchored on turquoise tropical water under a palm"></div>
    <div class="brand-mark">Tide and Tally<br>Dockside Boat Fair</div>
    <div class="headline"><span>Win a <span class="gold">tropical travel</span></span><span class="gold">voucher <span style="color:var(--white)">for</span> $2000</span><span class="more-info" style="font-size:17px;line-height:26px">More info</span></div>
  </div>

  <span class="size-label" style="left:920px;top:936px">300 x 250 pixel</span>

  <div class="ad sky" style="left:114px">
    <div class="photo photo-kids" role="img" aria-label="Two children in life jackets jumping on a pontoon boat sofa"></div>
    <div class="brand-mark">Tide and Tally<br>Dockside Boat Fair</div>
    <div class="headline" style="top:320px;bottom:30px"><span>Tide and Tally</span><span>Dockside Boat</span><span>Fair sets sail</span><span>on</span><span class="gold">Grand Lake, OK.</span><span class="gold">April 29th -</span><span class="gold">May 1st</span></div>
  </div>

  <div class="ad sky" style="left:306px">
    <div class="photo photo-boat" role="img" aria-label="Pontoon boat speeding across the lake"></div>
    <div class="brand-mark">Tide and Tally<br>Dockside Boat Fair</div>
    <div class="headline"><span><span class="gold">Over 100</span> new</span><span>and pre-owned</span><span>boats at</span><span class="gold">5 locations</span><span>and <span class="pink">7 boat</span></span><span class="pink">dealers</span></div>
  </div>

  <div class="ad sky" style="left:498px">
    <div class="photo photo-tropic" role="img" aria-label="Yacht on turquoise tropical water with palm fronds"></div>
    <div class="brand-mark" style="top:265px">Tide and Tally<br>Dockside Boat Fair</div>
    <div class="headline" style="top:380px;bottom:70px"><span>Win a <span class="gold">tropical</span></span><span class="gold">travel voucher</span><span>for <span class="gold">$2000</span></span><span class="more-info" style="font-size:17px;line-height:26px;margin-top:10px">More info</span></div>
  </div>

  <span class="size-label" style="left:387px;top:1055px">160 x 600 pixel</span>

</div>
</body>
</html>
```